Business Card Re-Design for a Lighting Designer

I would like my business card re-designed. It is currently high gloss and they scratch too easily. I don not think the current design lends itself well to a matte finish. I have included the current design for reference along with our company logo.
Check out our website for current branding.
http://www.brambleorchidstudio.example

Updates
Some of the top contenders are muslim and it is a holiday for them. I do not want to discriminate and would expect the same courtesy for holidays we celebrate.
Target Market(s)
Interior Designers, Architects
Contact Information for Business Card
Logo - Name, Title, Address, Telephone Number and Extension, Email
Font styles to use
Requirements
Must have
- All the information listed on the current business card. If you use Red, it needs to be the red from our logo.
Nice to have
- Vertical and Horizontal Designs will be entertained.
Should not have
- Requirements for a glossy finish...should not look too corporate since we are a design firm.

```html
<!DOCTYPE html>
<html lang="en">
<head>
<meta charset="utf-8">
<title>Bramble Orchid Studio — Business Card</title>
<link rel="stylesheet" href="https://fonts.googleapis.com/css2?family=Montserrat:wght@700&family=Questrial&family=Roboto+Condensed:wght@300;400&display=swap">
<style>
  :root {
    --stage: #e9e7e4;
    --card: #f6f6f6;
    --red: #e8141b;
    --brand-red: #9e2f30;
    --ink: #1e1e1e;
    --grey: #6f6f6f;
  }
  * { box-sizing: border-box; margin: 0; padding: 0; }
  html, body { width: 1200px; height: 900px; overflow: hidden; }
  body {
    background: var(--stage);
    display: flex;
    justify-content: center;
    align-items: center;
    gap: 90px;
    font-family: "Questrial", sans-serif;
    color: var(--ink);
  }
  .card {
    width: 360px;
    height: 620px;
    background: var(--card);
    box-shadow: 0 6px 22px rgba(0,0,0,.14);
    position: relative;
    display: flex;
    flex-direction: column;
    align-items: center;
  }

  /* front */
  .card-front { padding-top: 108px; }
  .person-name {
    font-family: "Montserrat", sans-serif;
    font-weight: 700;
    font-size: 30px;
    color: var(--red);
    letter-spacing: -0.5px;
  }
  .person-title {
    display: flex;
    align-items: center;
    gap: 4px;
    margin-top: 2px;
    font-family: "Roboto Condensed", sans-serif;
    font-size: 17px;
    color: var(--brand-red);
  }
  .title-rule { height: 4px; width: 82px; }
  .title-rule.left { background: linear-gradient(to right, transparent, var(--brand-red)); }
  .title-rule.right { background: linear-gradient(to left, transparent, var(--brand-red)); }
  .contact-list {
    list-style: none;
    margin-top: 68px;
    display: flex;
    flex-direction: column;
    align-items: center;
    gap: 40px;
    text-align: center;
    font-size: 15px;
  }
  .contact-item { display: flex; flex-direction: column; align-items: center; gap: 8px; }
  .contact-item svg { display: block; }
  .phone-number { font-family: "Roboto Condensed", sans-serif; font-size: 17px; }
  .email-domain { color: var(--brand-red); }
  .address { line-height: 1.3; font-size: 16px; }
  .front-band {
    position: absolute;
    bottom: 14px;
    left: 112px;
    right: 50px;
    height: 9px;
    background: var(--red);
  }

  /* back */
  .card-back { padding-top: 118px; }
  .brand-mark {
    display: flex;
    align-items: center;
    gap: 12px;
    font-family: "Roboto Condensed", sans-serif;
    font-weight: 400;
    font-size: 30px;
    line-height: 1.05;
    color: var(--ink);
  }
  .brand-square { width: 40px; height: 40px; background: var(--brand-red); flex: none; }
  .tag-rule {
    width: 130px;
    height: 3px;
    background: var(--red);
    margin-top: 162px;
  }
  .tagline {
    margin-top: 16px;
    border: 3px solid var(--red);
    padding: 5px 12px;
    font-family: "Roboto Condensed", sans-serif;
    font-weight: 300;
    font-size: 22px;
    color: var(--grey);
    white-space: nowrap;
  }
  .back-web {
    position: absolute;
    bottom: 52px;
    font-size: 15px;
    color: var(--red);
  }
</style>
</head>
<body>

  <section class="card card-front">
    <h1 class="person-name">MAREN HOLLOWAY</h1>
    <p class="person-title"><span class="title-rule left"></span>PRINCIPAL<span class="title-rule right"></span></p>

    <ul class="contact-list">
      <li class="contact-item">
        <svg width="18" height="30" viewBox="0 0 18 30" aria-hidden="true">
          <rect x="1" y="1" width="16" height="28" rx="2" fill="var(--red)"/>
          <circle cx="9" cy="25.5" r="1.2" fill="#fff"/>
          <rect x="6" y="3" width="6" height="1" fill="#fff"/>
        </svg>
        <span class="phone-number">555.014.2290 x1</span>
      </li>
      <li class="contact-item">
        <svg width="26" height="18" viewBox="0 0 26 18" aria-hidden="true">
          <rect x="0" y="0" width="26" height="18" fill="var(--red)"/>
          <path d="M1 1 L13 10 L25 1 M1 17 L10 8 M25 17 L16 8" stroke="#fff" stroke-width="1.5" fill="none"/>
        </svg>
        <span class="email">maren@<span class="email-domain">brambleorchidstudio</span>.example</span>
      </li>
      <li class="contact-item">
        <svg width="24" height="24" viewBox="0 0 24 24" aria-hidden="true">
          <circle cx="12" cy="12" r="10.5" fill="none" stroke="var(--red)" stroke-width="2"/>
          <ellipse cx="12" cy="12" rx="4.5" ry="10.5" fill="none" stroke="var(--red)" stroke-width="1.6"/>
          <path d="M2 12 H22 M4 7 H20 M4 17 H20" stroke="var(--red)" stroke-width="1.6"/>
        </svg>
        <span class="web">www.brambleorchidstudio.example</span>
      </li>
      <li class="contact-item">
        <svg width="18" height="26" viewBox="0 0 18 26" aria-hidden="true">
          <path d="M9 1 C4 1 1 4.6 1 9 C1 15 9 25 9 25 C9 25 17 15 17 9 C17 4.6 14 1 9 1 Z" fill="var(--red)"/>
          <circle cx="9" cy="9" r="3" fill="#fff"/>
        </svg>
        <span class="address">218 Larkspur Commons,<br>Suite 40 Fernbrook Vermont<br>05401 USA</span>
      </li>
    </ul>
    <div class="front-band"></div>
  </section>

  <section class="card card-back">
    <div class="brand-mark">
      <span class="brand-square"></span>
      <span class="brand-name">BRAMBLE<br>ORCHID STUDIO</span>
    </div>
    <div class="tag-rule"></div>
    <p class="tagline">LIGHTING FOR ARCHITECTURE</p>
    <p class="back-web">www.brambleorchidstudio.example</p>
  </section>

</body>
</html>
```